Comp & Pen Prep Tip Sheet for Veterans

I need a flyer/brochure/card with tips to help prepare veterans for their upcoming Comp & Pen Exams. Needs to be colorful and have vectors/images that correspond with teach tip. I have attached a word document with the language to include. This will go out with our welcome kit for veterans to reference before their exam.

Target Market(s)

Veterans

Industry/Entity Type

Legal/Non-Profit Organization/Medical

Colors
0054AA
0677BA
7BADD7
CADEEF
E8F1F8

Requirements
Must have
• Vectors/easy to follow

```html
<!DOCTYPE html>
<html lang="en">
<head>
<meta charset="utf-8">
<title>Comp &amp; Pen Exam Prep Tips for Veterans</title>
<link href="https://fonts.googleapis.com/css2?family=Oswald:wght@600;700&family=Barlow:wght@400;500;700;800&family=Arimo:wght@400&display=swap" rel="stylesheet">
<style>
:root{
  --blue:#1458a8;
  --blue-deep:#0054AA;
  --ink:#1d2430;
  --stage:#222835;
  --stage-light:#dbe8f4;
  --white:#ffffff;
  --black:#111111;
}
*{box-sizing:border-box;margin:0;padding:0}
html,body{width:1200px;height:2316px;overflow:hidden}
body{background:linear-gradient(var(--stage) 0 1540px,var(--stage-light) 1540px 2316px);position:relative;font-family:"Arimo",Arial,sans-serif}
.sheet{position:absolute;left:99px;top:59px;width:1000px;height:1413px;background:var(--blue)}
.abs{position:absolute}
.brand-box{left:31px;top:32px;width:438px;height:387px;background:var(--white);display:flex;flex-direction:column;align-items:center;justify-content:center;gap:20px}
.brand-mark{display:flex;align-items:center;gap:14px}
.brand-dot{width:44px;height:44px;border-radius:50%;background:var(--blue)}
.brand-name{font-family:"Oswald",sans-serif;font-weight:700;font-size:34px;color:var(--blue);line-height:1.1;text-align:left}
.brand-since{font-family:"Oswald",sans-serif;font-weight:600;font-size:17px;color:var(--black);letter-spacing:.3px}
.headline{left:56px;top:462px;color:var(--white);font-family:"Barlow",sans-serif;line-height:1}
.headline .l1{font-size:70px;font-weight:400;letter-spacing:1px}
.headline .l2{font-size:140px;font-weight:800;letter-spacing:-2px;margin-top:-2px}
.headline .l3{font-size:85px;font-weight:800;margin-top:-4px}
.headline .l4{font-size:59px;font-weight:400;letter-spacing:1px;margin-top:4px}
.intro{left:31px;top:858px;width:438px;height:437px;background:var(--white);padding:30px 22px 0 24px}
.intro li{list-style:none;display:flex;align-items:center;gap:18px;font-size:16.6px;line-height:20.2px;color:var(--ink);margin-bottom:33px}
.intro li:nth-child(2){margin-bottom:38px}
.intro svg{flex:none}
.url{left:40px;top:1332px;width:420px;display:flex;align-items:center;gap:16px;color:var(--white);font-family:"Barlow",sans-serif;font-weight:500;font-size:32px;letter-spacing:3px;white-space:nowrap}
.url .rule{flex:1;min-width:20px;height:2px;background:var(--white)}
.title-box{left:511px;top:32px;width:489px;height:228px;background:var(--white);padding:24px 0 0 46px}
.title-box h1{font-family:"Oswald",sans-serif;font-weight:700;font-size:56px;line-height:56px;color:var(--blue)}
.edge{left:980px;top:250px;width:20px;height:1080px;background:var(--white)}
.tip{left:566px;width:408px;background:var(--white);border:3px solid var(--blue);border-left:none;padding:18px 6px 0 97px}
.tip h2{font-family:"Oswald",sans-serif;font-weight:700;font-size:28px;color:var(--blue);margin-left:-38px;margin-bottom:16px;line-height:1}
.tip h2 span{display:inline-block;width:38px}
.tip p{font-size:11.4px;line-height:14.2px;color:var(--black);margin-bottom:14px}
.badge{width:136px;height:136px;border-radius:50%;background:var(--white);left:493px;display:flex;align-items:center;justify-content:center}
.badge .core{width:104px;height:104px;border-radius:50%;background:var(--blue);display:flex;align-items:center;justify-content:center}
</style>
</head>
<body>
<main class="sheet">
  <section class="abs brand-box">
    <div class="brand-mark"><span class="brand-dot"></span><span class="brand-name">Harbor Veterans<br>Alliance</span></div>
    <div class="brand-since">Serving Veterans Since 1993</div>
  </section>

  <section class="abs headline">
    <div class="l1">COMP &amp; PEN</div>
    <div class="l2">EXAM</div>
    <div class="l3">PREP TIPS</div>
    <div class="l4">FOR VETERANS</div>
  </section>

  <ul class="abs intro">
    <li><svg width="28" height="28" viewBox="0 0 28 28"><circle cx="14" cy="14" r="14" fill="#111"/><path d="M8 14.5l4 4 8-9" stroke="#fff" stroke-width="3" fill="none"/></svg><span>The Comp &amp; Pen Exam is your opportunity to present all the reasons you believe your condition is related to service to the physician.</span></li>
    <li><svg width="28" height="28" viewBox="0 0 28 28"><circle cx="14" cy="14" r="14" fill="#111"/><path d="M8 14.5l4 4 8-9" stroke="#fff" stroke-width="3" fill="none"/></svg><span>If your condition is not already service-connected, be sure to talk to the examiner about what happened in service that could have led to your current condition. The examiner will review your file, including your statements, service records, and treatment records, and provide a medical opinion as to whether your condition was caused or aggravated by your military service.</span></li>
    <li><svg width="28" height="28" viewBox="0 0 28 28"><circle cx="14" cy="14" r="14" fill="#111"/><path d="M8 14.5l4 4 8-9" stroke="#fff" stroke-width="3" fill="none"/></svg><span>The examiner will be observing your movements and behavior and may perform a limited physical exam to evaluate your condition.</span></li>
  </ul>

  <div class="abs url"><span class="rule"></span>www.harborvets.org<span class="rule"></span></div>

  <header class="abs title-box"><h1>Things to<br>Remember For<br>Your Exam</h1></header>
  <div class="abs edge"></div>

  <article class="abs tip" style="top:251px;height:187px">
    <h2><span>1.</span>Talk About Your Service</h2>
    <p>Talk about what happened in service that you believe caused or aggravated your condition. Try to be as specific as possible. If you are not comfortable discussing the details of an in-service event, you may point to statements you submitted to the VA previously for the examiner to reference. If you can, provide the examiner with a copy of these statements on the day of the exam</p>
  </article>
  <div class="abs badge" style="top:281px"><div class="core"><svg width="66" height="66" viewBox="0 0 66 66" fill="none" stroke="#fff" stroke-width="3" stroke-linejoin="round"><path d="M22 6h22v16L33 30 22 22z"/><circle cx="33" cy="45" r="15"/><path d="M33 36l3 6.5 7 .8-5.2 4.7 1.5 7L33 51.5 26.7 55l1.5-7L23 43.3l7-.8z"/></svg></div></div>

  <article class="abs tip" style="top:447px;height:165px">
    <h2><span>2.</span>Trace Your Symptoms</h2>
    <p>Discuss what symptoms you experienced immediately following your injury in service and how these symptoms have worsened over time.</p>
    <p>Your statement will help trace the start of your symptoms back to what happened during service.</p>
  </article>
  <div class="abs badge" style="top:462px"><div class="core"><svg width="66" height="66" viewBox="0 0 66 66" fill="none" stroke="#fff" stroke-width="3" stroke-linecap="round" stroke-linejoin="round"><rect x="8" y="10" width="50" height="38" rx="4"/><path d="M14 34h8l5-12 7 20 5-10h13"/><circle cx="46" cy="52" r="9" fill="#1458a8"/><path d="M42 52l3 3 5-6"/></svg></div></div>

  <article class="abs tip" style="top:621px;height:187px">
    <h2><span>3.</span>Be Honest.</h2>
    <p>Be honest when describing the frequency and severity of your symptoms and how they impact your day-to-day life to the examiner; do not downplay the severity of your symptoms.</p>
    <p>Keep in mind that the examiner will be closely monitoring your movements and behavior, including your body language and the tone of your voice.</p>
  </article>
  <div class="abs badge" style="top:653px"><div class="core"><svg width="64" height="64" viewBox="0 0 64 64" fill="none" stroke="#fff" stroke-width="3"><path d="M32 40C20 31 16 25 16 19a8 8 0 0 1 16-2 8 8 0 0 1 16 2c0 6-4 12-16 21z"/><path d="M8 34l10 14 8 6M56 34L46 48l-8 6"/></svg></div></div>

  <article class="abs tip" style="top:818px;height:185px">
    <h2><span>4.</span>Pain</h2>
    <p>While the exam is not meant to be painful, you may experience slight discomfort depending on the required testing.</p>
    <p>When testing your range of motion, be sure to tell the examiner AS SOON AS you begin to experience pain, as this contributes to your overall functional loss and should be considered in your rating.</p>
  </article>
  <div class="abs badge" style="top:848px"><div class="core"><svg width="64" height="64" viewBox="0 0 64 64" fill="none" stroke="#fff" stroke-width="3" stroke-linejoin="round"><path d="M36 6L22 32h12l-6 26 18-30H34z"/><path d="M10 40l8 4-6 6 8 2M54 40l-8 4 6 6-8 2"/></svg></div></div>

  <article class="abs tip" style="top:1014px;height:163px">
    <h2><span>5.</span>Ask for Clarification</h2>
    <p>Do not answer a question you do not understand. Ask for clarification if necessary. Do not talk to fill the space or time. Keep your conversation with the examiner limited to what happened in service, the frequency and severity of symptoms related to your condition, and how they impact your day-to-day life.</p>
  </article>
  <div class="abs badge" style="top:1044px"><div class="core"><svg width="68" height="68" viewBox="0 0 68 68" fill="none" stroke="#fff" stroke-width="3" stroke-linecap="round"><path d="M34 6a27 27 0 1 0 12 51l6 6V50A27 27 0 0 0 34 6z"/><path d="M20 30h28M20 40h18"/></svg></div></div>

  <article class="abs tip" style="top:1187px;height:181px">
    <h2><span>6.</span>Medications</h2>
    <p>If you are prescribed any medication(s) for your condition, be sure to tell the examiner the name and dosage of each medication and how often you take each. This is extremely important, because medication may mask some of your symptoms, or the use of medication(s) may be used to evaluate the severity of your condition and how much it impacts your ability to work.</p>
  </article>
  <div class="abs badge" style="top:1222px"><div class="core"><svg width="70" height="70" viewBox="0 0 70 70" fill="none" stroke="#fff" stroke-width="3"><rect x="12" y="6" width="24" height="58" rx="12"/><path d="M12 35h24"/><circle cx="46" cy="40" r="16"/><path d="M30 40h32"/></svg></div></div>
</main>
</body>
</html>
```